Redesign My Travel Voucher Coupons-Please redesign the flyers I have attached to this brief.

These designs will be catered towards like travel agency vacation stays...luxury resort stays, hotel and airfare getaways, etc. so must have a travel theme but more importantly professional trustworthy appeal...

Please redesign the flyers I have attached to this brief.

I have attached my existing designs. Please use all existing content and elements exactly but make the design much better...also, please keep in mind that these would be full color and printer friendly...

Target Market(s)

Consumers. People receive these vouchers from businesses that run marketing promotions and contests and giveaways. So the look and feel must feel professional and trustworthy but not cheesy and fake.

Industry/Entity Type

Hotel

Requirements
Must have
• Please use all existing content and elements exactly but make the design much better...also, please keep in mind that these would be full color and printer friendly...

MUST HAVE ALL EXISTING CONTENT EXACT NO EXCEPTIONS
Nice to have
• These designs will be catered towards like travel agency vacation stays...luxury resort stays, hotel and airfare getaways, etc. so must have a travel theme but more importantly professional trustworthy appeal...

Should not have

```html
<!DOCTYPE html>
<html lang="en">
<head>
<meta charset="utf-8">
<title>Enjoy Airfare With Hotel – Travel Voucher Flyers</title>
<link rel="stylesheet" href="https://fonts.googleapis.com/css2?family=Oswald:wght@400;500;600&family=Roboto+Condensed:ital,wght@0,300;0,400;0,700;1,400;1,700&family=Courier+Prime&family=Roboto:wght@400;700&display=swap">
<style>
  :root{
    --page-bg:#b9b9b9;
    --label:#4a4a4a;
    --blue:#1a63d0;
    --blue-bright:#2f86ea;
    --sky-top:#5fa4e6;
    --sky-bottom:#e4eef7;
    --pale-blue:rgba(214,232,250,.92);
    --dark:#201c1c;
    --ink:#2a2a2a;
    --light-band:#efefef;
    --pill-light:#ececec;
    --white:#ffffff;
  }
  *{margin:0;padding:0;box-sizing:border-box}
  html,body{width:1200px;height:870px;overflow:hidden;background:var(--page-bg)}
  .stage{position:absolute;left:0;top:0;width:2068px;height:1500px;transform:scale(.5803);transform-origin:0 0}
  .sheet-label{position:absolute;top:30px;left:0;width:100%;text-align:center;font:600 100px/1 "Oswald",sans-serif;color:var(--label);letter-spacing:-1px}
  .flyer{position:absolute;top:247px;width:893px;height:1156px;overflow:hidden;box-shadow:0 4px 14px rgba(0,0,0,.25);font-family:"Roboto Condensed",sans-serif}
  .flyer--dark{left:102px;background:var(--dark);color:var(--white)}
  .flyer--light{left:1083px;background:var(--white);color:var(--ink)}
  .flyer > *{position:absolute}
  .hero-photo{left:0;top:0;width:893px;height:360px;background:linear-gradient(180deg,var(--sky-top) 0%,#a9cbec 45%,var(--sky-bottom) 100%)}
  .hero-shapes{left:0;top:0;width:893px;height:1156px}
  .title-bar{left:0;top:29px;width:604px;height:70px;background:var(--blue);color:var(--white);font:500 52px/70px "Oswald",sans-serif;padding-left:44px;letter-spacing:-.5px}
  .subtitle{left:0;top:100px;width:500px;height:70px;background:var(--pale-blue);color:#1e2a38;font:300 30px/29px "Roboto Condensed",sans-serif;padding:6px 0 0 44px}
  .exclusive{left:70px;top:295px;font:italic 700 16px/1 "Roboto Condensed",sans-serif}
  .flyer--light .exclusive{color:var(--blue-bright)}
  .name-field{left:45px;top:318px;width:482px;height:40px;border-radius:20px;background:var(--white)}
  .flyer--light .name-field{background:var(--pill-light)}
  .intro{left:47px;top:373px;width:810px;font:400 17px/23.3px "Roboto Condensed",sans-serif;text-align:justify}
  .features-band{left:0;top:500px;width:893px;height:176px;background:var(--light-band)}
  .features-title{left:0;top:484px;width:893px;text-align:center;font:500 30px/36px "Oswald",sans-serif;letter-spacing:3px;color:var(--blue-bright)}
  .flyer--light .features-title{left:327px;width:203px;background:var(--blue-bright);color:var(--white);border-radius:18px}
  .rule{left:47px;width:807px;height:3px;background:var(--blue)}
  .feature-list{list-style:none;font:400 15px/29px "Roboto Condensed",sans-serif}
  .feature-list li{display:flex;align-items:center;gap:6px;white-space:nowrap}
  .feature-list svg{width:14px;height:14px;flex:none}
  .section-title{left:45px;font:500 30px/1 "Oswald",sans-serif;letter-spacing:3px;color:var(--blue-bright)}
  .flyer--light .section-title{color:#3a3a3a}
  .how-text{left:47px;top:723px;width:503px;font:400 14.3px/17.5px "Roboto Condensed",sans-serif;text-align:justify;letter-spacing:-.35px}
  .travel-photo{left:568px;top:714px;width:286px;height:316px;background:linear-gradient(160deg,#3e4b57 0%,#8a6b44 45%,#e8b368 60%,#3b3f46 100%)}
  .quote{left:47px;top:919px;width:483px;text-align:center;font:italic 400 15px/16px "Roboto Condensed",sans-serif;letter-spacing:-.2px}
  .quote-name{display:block;font-style:normal}
  .coupon{left:0;top:1012px;width:558px;height:144px;background:var(--white);border-top:2px dashed #333;border-right:2px dashed #333;color:#1b1b1b}
  .coupon > *{position:absolute}
  .coupon-title{left:0;top:6px;width:558px;text-align:center;font:500 38px/1.1 "Oswald",sans-serif;color:var(--blue)}
  .expires{left:52px;top:56px;width:100px;text-align:center;font:400 15px/15px "Courier Prime",monospace}
  .voucher-no{left:28px;top:120px;font:400 15px/1 "Courier Prime",monospace;letter-spacing:1px}
  .redeem{left:230px;top:60px;font:400 15px/16px "Oswald",sans-serif}
  .redeem strong{display:block;font:600 19px/22px "Oswald",sans-serif}
  .redeem em{display:block;font:italic 400 12px/16px "Roboto Condensed",sans-serif;margin-top:2px}
  .sponsor{left:632px;top:992px;width:184px;height:80px;border-radius:50%;background:var(--white);border:4px solid #1b1b1b;text-align:center;color:#1b1b1b}
  .sponsor-lead{display:block;font:italic 700 12px/1 "Roboto Condensed",sans-serif;margin-top:12px}
  .sponsor-name{display:block;font:700 15px/1 "Roboto Condensed",sans-serif;color:var(--blue);margin-top:10px}
  .contact{left:590px;top:1088px;width:280px;text-align:center;font:400 15px/18px "Roboto",sans-serif}
  .contact strong{display:block;font-weight:700}
</style>
</head>
<body>
<main class="stage">
  <h1 class="sheet-label">FLYER#7</h1>

  <article class="flyer flyer--dark">
    <div class="hero-photo" role="img" aria-label="Jumbo passenger jet flying over a bright blue sky with clouds"></div>
    <svg class="hero-shapes" viewBox="0 0 893 1156" aria-hidden="true">
      <polygon points="0,345 92,222 893,292 893,348" fill="var(--blue-bright)"/>
      <polygon points="0,350 100,243 893,348 893,1156 0,1156" fill="var(--dark)"/>
    </svg>
    <h2 class="title-bar">ENJOY AIRFARE WITH HOTEL</h2>
    <p class="subtitle">TWO ROUNDTRIP AIRFARE WITH<br>2 NIGHTS HOTEL ACCOMMODATIONS</p>
    <p class="exclusive">EXCLUSIVELY FOR:</p>
    <div class="name-field"></div>
    <p class="intro">Congratulations, you and a guest will receive round trip airfare tickets with two nights of hotel accommodations. Our destination cities include: Las Vegas, Reno, Phoenix, Denver, Chicago, Atlantic City (flying into Philadelphia, PA), Orlando, Miami, Tampa, Fort Lauderdale, Atlanta, Baltimore, Washington DC, Minneapolis, St Louis, Los Angeles, Anaheim, San Diego, New Orleans, Philadelphia, Dallas, Houston and Nashville!</p>
    <h3 class="features-title">FEATURES</h3>
    <div class="rule" style="top:523px"></div>
    <ul class="feature-list" style="left:75px;top:525px">
      <li><svg viewBox="0 0 14 14"><polyline points="2,7 6,11 12,2" fill="none" stroke="var(--blue-bright)" stroke-width="2.5"/></svg>Two Roundtrip Airfare</li>
      <li><svg viewBox="0 0 14 14"><polyline points="2,7 6,11 12,2" fill="none" stroke="var(--blue-bright)" stroke-width="2.5"/></svg>23 Exciting Vacation Destinations To Choose From</li>
      <li><svg viewBox="0 0 14 14"><polyline points="2,7 6,11 12,2" fill="none" stroke="var(--blue-bright)" stroke-width="2.5"/></svg>24 Months To Complete Travel After Redemption</li>
      <li><svg viewBox="0 0 14 14"><polyline points="2,7 6,11 12,2" fill="none" stroke="var(--blue-bright)" stroke-width="2.5"/></svg>Just Pay Taxes &amp; Fees</li>
      <li><svg viewBox="0 0 14 14"><polyline points="2,7 6,11 12,2" fill="none" stroke="var(--blue-bright)" stroke-width="2.5"/></svg>No timeshares or sales presentations, Guaranteed!</li>
    </ul>
    <ul class="feature-list" style="left:480px;top:525px">
      <li><svg viewBox="0 0 14 14"><polyline points="2,7 6,11 12,2" fill="none" stroke="var(--blue-bright)" stroke-width="2.5"/></svg>Two Nights Hotel Accommodations Included</li>
      <li><svg viewBox="0 0 14 14"><polyline points="2,7 6,11 12,2" fill="none" stroke="var(--blue-bright)" stroke-width="2.5"/></svg>Redeem Now, Travel Later</li>
      <li><svg viewBox="0 0 14 14"><polyline points="2,7 6,11 12,2" fill="none" stroke="var(--blue-bright)" stroke-width="2.5"/></svg>Transferrable To Another Person</li>
      <li><svg viewBox="0 0 14 14"><polyline points="2,7 6,11 12,2" fill="none" stroke="var(--blue-bright)" stroke-width="2.5"/></svg>Book By Phone With A Travel Agent</li>
    </ul>
    <div class="rule" style="top:672px"></div>
    <h3 class="section-title" style="top:690px">HOW CAN WE DO THIS?</h3>
    <p class="how-text">We contract with the world leading hotel chains and resorts to help them fill their otherwise empty rooms. We help fill empty rooms which the hotels, resorts and cruise lines turn into additional revenue from other areas of their property and future bookings. Hotels rarely experience full occupancy, yet they remain open, providing rooms and services at fixed costs. So when hotels give out their rooms by partnering with marketing companies like us, they might miss out on the room fee, but they already didn't have that in the first place, at least now they have the opportunity to gain a customer for their in-house restaurants, room service, their casinos, an extra day stay, future bookings, etc.</p>
    <div class="travel-photo" role="img" aria-label="Traveller at an airport gate window watching a plane take off at sunset"></div>
    <h3 class="section-title" style="top:884px">WHAT OTHERS SAY?</h3>
    <p class="quote">"Being able to stay right on the strip in Las Vegas was great. I love that we were able to walk around to all the sites and attractions. The fountains at the Aurelia were AMAZING! The Gondola ride at the Laguna was very nice. I LOVED the atmosphere and the food. The whole experience was awesome, THANK YOU!"<span class="quote-name">Melissa R. San Diego, CA</span></p>
    <section class="coupon">
      <h2 class="coupon-title">ENJOY AIRFARE WITH HOTEL</h2>
      <p class="expires">EXPIRES<br>11/07/2020</p>
      <p class="voucher-no">107083-11293</p>
      <p class="redeem">VIEW ALL THE DETAILS OF THIS<br>SPECIAL OFFER AND REDEEM ONLINE AT<strong>WWW.TRAVELPERKSONLINE.COM</strong><em>*Terms and Conditions apply see website for details</em></p>
    </section>
    <div class="sponsor"><span class="sponsor-lead">Compliments Of</span><span class="sponsor-name">Bright Path Rewards</span></div>
    <p class="contact">Dana Whitfield &nbsp;|&nbsp; 555-204-3187<strong>www.BrightPathPromos.com</strong></p>
  </article>

  <article class="flyer flyer--light">
    <div class="hero-photo" role="img" aria-label="Jumbo passenger jet flying over a bright blue sky with clouds"></div>
    <svg class="hero-shapes" viewBox="0 0 893 1156" aria-hidden="true">
      <polygon points="0,345 92,222 893,292 893,348" fill="var(--blue-bright)"/>
      <polygon points="0,350 100,243 893,348 893,1156 0,1156" fill="var(--white)"/>
    </svg>
    <div class="features-band"></div>
    <h2 class="title-bar">ENJOY AIRFARE WITH HOTEL</h2>
    <p class="subtitle">TWO ROUNDTRIP AIRFARE WITH<br>2 NIGHTS HOTEL ACCOMMODATIONS</p>
    <p class="exclusive">EXCLUSIVELY FOR:</p>
    <div class="name-field"></div>
    <p class="intro">Congratulations, you and a guest will receive round trip airfare tickets with two nights of hotel accommodations. Our destination cities include: Las Vegas, Reno, Phoenix, Denver, Chicago, Atlantic City (flying into Philadelphia, PA), Orlando, Miami, Tampa, Fort Lauderdale, Atlanta, Baltimore, Washington DC, Minneapolis, St Louis, Los Angeles, Anaheim, San Diego, New Orleans, Philadelphia, Dallas, Houston and Nashville!</p>
    <h3 class="features-title">FEATURES</h3>
    <ul class="feature-list" style="left:75px;top:525px">
      <li><svg viewBox="0 0 14 14"><polyline points="2,7 6,11 12,2" fill="none" stroke="var(--blue-bright)" stroke-width="2.5"/></svg>Two Roundtrip Airfare</li>
      <li><svg viewBox="0 0 14 14"><polyline points="2,7 6,11 12,2" fill="none" stroke="var(--blue-bright)" stroke-width="2.5"/></svg>23 Exciting Vacation Destinations To Choose From</li>
      <li><svg viewBox="0 0 14 14"><polyline points="2,7 6,11 12,2" fill="none" stroke="var(--blue-bright)" stroke-width="2.5"/></svg>24 Months To Complete Travel After Redemption</li>
      <li><svg viewBox="0 0 14 14"><polyline points="2,7 6,11 12,2" fill="none" stroke="var(--blue-bright)" stroke-width="2.5"/></svg>Just Pay Taxes &amp; Fees</li>
      <li><svg viewBox="0 0 14 14"><polyline points="2,7 6,11 12,2" fill="none" stroke="var(--blue-bright)" stroke-width="2.5"/></svg>No timeshares or sales presentations, Guaranteed!</li>
    </ul>
    <ul class="feature-list" style="left:480px;top:525px">
      <li><svg viewBox="0 0 14 14"><polyline points="2,7 6,11 12,2" fill="none" stroke="var(--blue-bright)" stroke-width="2.5"/></svg>Two Nights Hotel Accommodations Included</li>
      <li><svg viewBox="0 0 14 14"><polyline points="2,7 6,11 12,2" fill="none" stroke="var(--blue-bright)" stroke-width="2.5"/></svg>Redeem Now, Travel Later</li>
      <li><svg viewBox="0 0 14 14"><polyline points="2,7 6,11 12,2" fill="none" stroke="var(--blue-bright)" stroke-width="2.5"/></svg>Transferrable To Another Person</li>
      <li><svg viewBox="0 0 14 14"><polyline points="2,7 6,11 12,2" fill="none" stroke="var(--blue-bright)" stroke-width="2.5"/></svg>Book By Phone With A Travel Agent</li>
    </ul>
    <h3 class="section-title" style="top:690px">HOW CAN WE DO THIS?</h3>
    <p class="how-text">We contract with the world leading hotel chains and resorts to help them fill their otherwise empty rooms. We help fill empty rooms which the hotels, resorts and cruise lines turn into additional revenue from other areas of their property and future bookings. Hotels rarely experience full occupancy, yet they remain open, providing rooms and services at fixed costs. So when hotels give out their rooms by partnering with marketing companies like us, they might miss out on the room fee, but they already didn't have that in the first place, at least now they have the opportunity to gain a customer for their in-house restaurants, room service, their casinos, an extra day stay, future bookings, etc.</p>
    <div class="travel-photo" role="img" aria-label="Traveller at an airport gate window watching a plane take off at sunset"></div>
    <h3 class="section-title" style="top:884px">WHAT OTHERS SAY?</h3>
    <p class="quote">"Being able to stay right on the strip in Las Vegas was great. I love that we were able to walk around to all the sites and attractions. The fountains at the Aurelia were AMAZING! The Gondola ride at the Laguna was very nice. I LOVED the atmosphere and the food. The whole experience was awesome, THANK YOU!"<span class="quote-name">Melissa R. San Diego, CA</span></p>
    <section class="coupon">
      <h2 class="coupon-title">ENJOY AIRFARE WITH HOTEL</h2>
      <p class="expires">EXPIRES<br>11/07/2020</p>
      <p class="voucher-no">107083-11293</p>
      <p class="redeem">VIEW ALL THE DETAILS OF THIS<br>SPECIAL OFFER AND REDEEM ONLINE AT<strong>WWW.TRAVELPERKSONLINE.COM</strong><em>*Terms and Conditions apply see website for details</em></p>
    </section>
    <div class="sponsor"><span class="sponsor-lead">Compliments Of</span><span class="sponsor-name">Bright Path Rewards</span></div>
    <p class="contact">Dana Whitfield &nbsp;|&nbsp; 555-204-3187<strong>www.BrightPathPromos.com</strong></p>
  </article>
</main>
</body>
</html>
```